Business Card: RW Office Partners - Your tidy answer finder

Business Name: RW Office Partners
Website: www.rwofficepartners.com.au
Email: marisol@rwofficepartners.com.au
Mobile: 61 487 902 346
Facebook: @rwofficepartners
Instrgram: @rwofficepartners

Brading Colours:
HEX
#986474
#ddccd3
#7a8498
#c9d8e4
#000000
#ffffff

Tag Line: Your organised problem solver

Link to DRAFT website:
https://helpdeskhub.sitebuilderx.com/rw-office-partners

About Page from the website:
My name is Marisol Bramwell, and I would love to assist you to become more productive in your day to day and achieve your business and personal goals.
My mission is to give you time, time to work on the important tasks of your business or to be able to spend more time with your family. I will take on the tasks you don’t have time for, don’t know well or simply don’t like to do.
I have an extensive background in Administration, Tender Coordination, Document Control, WHS and Quality Management working primarily in the Construction, Mining and Corporate World.
I am passionate about being organised, having order and making things in your life (and mine) easier! I love to watch something unfold and grow into something amazing! I am known for being the go-to problem solver, the organiser of all things, producing high standards of work even under pressure. I’m also a confident communicator, and I understand that you’re busy running your business.

Target Market(s)

Small to Medium Business who require assistance in their business by a virtual assistant.

Industry/Entity Type

Virtual Assistant

Contact Information for Business Card

Mobile: 61 487 902 346

Font styles to use
Sans Serif

Colors
ffffff

Requirements
Must have
• Branding Colours as outlined.
Contact Details as outlined.
Logo as provided.
Proper contact details - mobile, facebook, instragm, website.
Simple, Elegant, very clean looking.
Should not have
• Note cute with pictures.
Not too girly as still want to market to construction companies.

```html
<!DOCTYPE html>
<html lang="en">
<head>
<meta charset="utf-8">
<title>RW Office Partners – Business Card</title>
<link href="https://fonts.googleapis.com/css2?family=Lato:wght@400;700&display=swap" rel="stylesheet">
<style>
  :root {
    --brand-rose: #986474;
    --brand-rose-soft: #ddccd3;
    --brand-slate: #7a8498;
    --brand-mist: #c9d8e4;
    --card-face: #f4efec;
    --backdrop: #e6e1dd;
    --ink-light: #ffffff;
    --ink-muted: #5a5258;
  }
  * { margin: 0; padding: 0; box-sizing: border-box; }
  html, body {
    width: 1200px; height: 1047px; overflow: hidden;
    background: var(--backdrop);
    font-family: "Lato", Arial, sans-serif;
  }
  .card {
    position: absolute; left: 100px; top: 238px;
    width: 1000px; height: 570px;
    background: var(--card-face);
    border-radius: 26px;
    overflow: hidden;
    box-shadow: 0 10px 30px rgba(60, 40, 50, 0.12);
  }
  .accent-rule {
    position: absolute; left: 0; right: 0; top: 300px; height: 6px;
    background: var(--brand-slate);
  }
  .contact-band {
    position: absolute; left: 0; right: 0; top: 318px; bottom: 0;
    background: var(--brand-rose);
  }
  .holder { position: absolute; left: 51px; top: 52px; }
  .holder-name {
    color: var(--brand-rose); font-weight: 700; font-size: 41px;
    letter-spacing: 0.5px; line-height: 1;
  }
  .holder-role {
    color: var(--ink-muted); font-size: 23px; margin-top: 14px;
  }
  .brand-name {
    position: absolute; right: 44px; top: 205px;
    color: var(--brand-rose); font-weight: 700; font-size: 46px;
    letter-spacing: 0.5px; line-height: 1;
  }
  .contact-list {
    position: absolute; left: 40px; top: 360px; list-style: none;
  }
  .contact-item {
    display: flex; align-items: center; height: 38px;
    color: var(--ink-light); font-size: 25px;
  }
  .contact-icon { width: 36px; height: 26px; margin-right: 16px; flex: none; }
</style>
</head>
<body>
  <section class="card" aria-label="RW Office Partners business card">
    <div class="accent-rule" aria-hidden="true"></div>
    <div class="contact-band" aria-hidden="true"></div>

    <header class="holder">
      <h1 class="holder-name">DANA WHITFIELD</h1>
      <p class="holder-role">Founder &amp; CEO</p>
    </header>

    <p class="brand-name">RW Office Partners</p>

    <ul class="contact-list">
      <li class="contact-item">
        <svg class="contact-icon" viewBox="0 0 36 26" aria-hidden="true"><path d="M11 5 c-3 1 -3 5 0 10 c3 5 7 7 10 6 l1 -3 l-4 -2 l-2 2 c-2 -1 -4 -4 -5 -6 l2 -2 l-2 -4 z" fill="none" stroke="#fff" stroke-width="1.8" stroke-linejoin="round"/><path d="M19 6 a6 6 0 0 1 5 5 M19 2 a10 10 0 0 1 9 9" fill="none" stroke="#fff" stroke-width="1.6"/></svg>
        <span>61 487 902 346</span>
      </li>
      <li class="contact-item">
        <svg class="contact-icon" viewBox="0 0 36 26" aria-hidden="true"><rect x="7" y="6" width="22" height="15" fill="#fff"/><polyline points="7,6 18,15 29,6" fill="none" stroke="var(--brand-rose)" stroke-width="1.8"/></svg>
        <span>marisol@rwofficepartners.com.au</span>
      </li>
      <li class="contact-item">
        <svg class="contact-icon" viewBox="0 0 36 26" aria-hidden="true"><g fill="none" stroke="#fff" stroke-width="1.6"><circle cx="18" cy="13" r="10"/><ellipse cx="18" cy="13" rx="4.5" ry="10"/><line x1="8" y1="13" x2="28" y2="13"/><line x1="10" y1="8" x2="26" y2="8"/><line x1="10" y1="18" x2="26" y2="18"/></g></svg>
        <span>www.rwofficepartners.com.au</span>
      </li>
      <li class="contact-item">
        <svg class="contact-icon" viewBox="0 0 36 26" aria-hidden="true"><circle cx="18" cy="13" r="10" fill="none" stroke="#fff" stroke-width="1.6"/></svg>
        <span>@rwofficepartners</span>
      </li>
      <li class="contact-item">
        <svg class="contact-icon" viewBox="0 0 36 26" aria-hidden="true"><circle cx="18" cy="13" r="10" fill="none" stroke="#fff" stroke-width="1.6"/></svg>
        <span>@rwofficepartners</span>
      </li>
    </ul>
  </section>
</body>
</html>
```